LoweniasMassage website required

We need a website for a mobile sports massage therapist in the United Kingdom. Specialising in pregnancy and postnatal massage, sports and remedial, deep tissue massage & Corprate Massage. Attached are some logos that we already have in various colours. The file named logo_white_background is what we normally use. Feel free to use the others at your discretion.

Requirements
Must have
• Service areas, Booking system.

```html
<!DOCTYPE html>
<html lang="en">
<head>
<meta charset="utf-8">
<title>Lowenia's Massage</title>
<link rel="stylesheet" href="https://fonts.googleapis.com/css2?family=M+PLUS+1p:wght@300;400;500;700&display=swap">
<style>
:root{
  --sky:#74cbf9;
  --sky-deep:#5fc0f4;
  --white:#ffffff;
  --ink:#1d1d1d;
  --skin-light:#e9c7b0;
  --skin-mid:#c98f6c;
  --studio:#d9d4cc;
  --footer-a:#e8ddd3;
  --footer-b:#c9b7a6;
}
*{box-sizing:border-box;margin:0;padding:0}
html,body{width:1200px;height:3193px;overflow:hidden}
body{position:relative;font-family:"M PLUS 1p",sans-serif;background:var(--white);color:var(--ink)}
.abs{position:absolute}
.site-header{left:0;top:0;width:1200px;height:153px;background:var(--sky)}
.brand{left:0;width:1200px;top:40px;text-align:center;color:var(--white);font-weight:500;font-size:34px;letter-spacing:2px}
.nav{left:0;top:122px;width:1200px;text-align:center;color:var(--white);font-size:24px;font-weight:500}
.nav a{color:var(--white);text-decoration:none;margin:0 16px}
.hero{left:0;top:153px;width:1200px;height:508px;background:linear-gradient(100deg,var(--studio) 0%,var(--skin-mid) 30%,var(--skin-light) 55%,#f1ece6 80%,#fbfaf8 100%)}
.hero-word{left:0;width:1200px;text-align:center;font-size:50px;font-weight:300;color:var(--sky)}
.btn{display:flex;align-items:center;justify-content:center;background:var(--sky);color:var(--white);border-radius:4px}
.hero-btn{left:486px;top:537px;width:236px;height:77px;font-size:26px;font-weight:500;border-radius:6px}
.about{left:0;top:661px;width:1200px;height:620px;background:var(--sky)}
.section-title{left:0;width:1200px;text-align:center;font-size:34px;font-weight:500}
.about .section-title{top:8px;color:var(--white)}
.portrait{left:215px;top:78px;width:386px;height:497px;border-radius:10px;background:linear-gradient(160deg,#3a2a22 0%,#5a3d2c 40%,#1e1c1f 100%)}
.about-text{left:635px;top:92px;width:350px;font-size:21px;line-height:33px;font-weight:300;color:var(--white)}
.services{left:0;top:1281px;width:1200px;height:818px;background:var(--white)}
.services .section-title{top:12px;color:var(--sky)}
.svc-art{background:linear-gradient(180deg,#e6f6fe,#bfe6fc);border-radius:8px}
.svc-name{text-align:center;font-size:16px;font-weight:500;color:var(--ink);width:400px}
.svc-desc{text-align:center;font-size:16px;line-height:33px;color:var(--sky);width:400px}
.svc-btn{height:38px;width:158px;font-size:15px}
.booking{left:0;top:2099px;width:1200px;height:727px;background:var(--sky)}
.booking .section-title{top:14px;color:var(--white)}
.form-card{left:377px;top:60px;width:446px;height:650px;background:var(--white);border-radius:12px}
.field{border:3px solid var(--sky);border-radius:6px;display:flex;align-items:center;font-size:19px;color:var(--ink)}
.select{left:24px;top:25px;width:398px;height:75px;padding-left:22px;font-size:21px}
.select svg{position:absolute;right:28px;top:26px}
.input{left:41px;width:356px;height:69px;padding-left:25px}
.date-box{width:45px;height:45px;border:3px solid var(--sky);border-radius:4px;display:flex;align-items:center;justify-content:center;font-size:16px}
.book-btn{left:77px;top:550px;width:279px;height:76px;font-size:28px;font-weight:500}
.footer{left:0;top:2826px;width:1200px;height:367px;background:linear-gradient(90deg,var(--footer-a) 0%,#f0e9e2 40%,var(--footer-b) 75%,#9d8a7a 100%)}
.contact{left:215px;top:112px;font-size:22px;line-height:35px;color:var(--ink)}
.contact .label{font-size:25px}
.social{display:flex;gap:10px;margin-top:6px}
.social span{width:32px;height:32px;border-radius:50%;background:var(--ink)}
.address{left:788px;top:62px;font-size:19px;line-height:33px;color:var(--ink)}
.address .label{font-size:25px;line-height:40px}
</style>
</head>
<body>
<header class="site-header abs">
  <div class="brand abs">Lowenia's Massage</div>
  <nav class="nav abs"><a href="#">Home</a><a href="#">About</a><a href="#">Services</a><a href="#">Booking</a><a href="#">Contact</a></nav>
</header>

<section class="hero abs" role="img" aria-label="Photo of a therapist massaging a client's shoulder">
  <div class="hero-word abs" style="top:95px">Relax</div>
  <div class="hero-word abs" style="top:197px">Enjoy</div>
  <div class="hero-word abs" style="top:296px">Rejuvenate</div>
  <div class="btn hero-btn abs" style="top:384px">Get Started</div>
</section>

<section class="about abs">
  <h2 class="section-title abs">About Lowenia</h2>
  <div class="portrait abs" role="img" aria-label="Portrait photo of the therapist seated at a table"></div>
  <p class="about-text abs">Proin gravida nibh vel velit auctor aliquet. Aenean sollicitudin, lorem quis bibendum auctor, nisi elit consequat ipsum, nec sagittis sem nibh id elit. Duis sed odio sit amet nibh vulputate cursus a sit amet mauris. Morbi accumsan ipsum velit. Nam nec tellus a odio tincidunt auctor a ornare odio. Sed non mauris vitae erat consequat auctor eu in elit. Class aptent taciti sociosqu ad litora torquent per conubia nostra, p.</p>
</section>

<section class="services abs">
  <h2 class="section-title abs">Services</h2>

  <div class="svc-art abs" style="left:341px;top:119px;width:85px;height:139px" role="img" aria-label="Line illustration of a pregnant woman"></div>
  <div class="svc-name abs" style="left:194px;top:258px">Pregnancy and post natal massage</div>
  <div class="svc-desc abs" style="left:194px;top:286px">Gentle relaxing massage<br>for a woman during<br>and after pregnancy</div>
  <div class="btn svc-btn abs" style="left:313px;top:394px">Book massage</div>

  <div class="svc-art abs" style="left:697px;top:119px;width:173px;height:134px" role="img" aria-label="Line illustration of a massage on a table"></div>
  <div class="svc-name abs" style="left:584px;top:256px">Deep tissue massage</div>
  <div class="svc-desc abs" style="left:584px;top:286px">Soothing massage to<br>relax all the tense areas</div>
  <div class="btn svc-btn abs" style="left:701px;top:394px">Book massage</div>

  <div class="svc-art abs" style="left:341px;top:477px;width:132px;height:134px;border-radius:50%" role="img" aria-label="Illustration of a football"></div>
  <div class="svc-name abs" style="left:207px;top:622px">Sports massage</div>
  <div class="svc-desc abs" style="left:207px;top:655px">Massage and stretching<br>to improve muscle flexibility<br>and faster recovery</div>
  <div class="btn svc-btn abs" style="left:326px;top:756px">Book massage</div>

  <div class="svc-art abs" style="left:735px;top:492px;width:96px;height:130px" role="img" aria-label="Line illustration of an office worker"></div>
  <div class="svc-name abs" style="left:584px;top:636px">Corporate massage</div>
  <div class="svc-desc abs" style="left:584px;top:672px">Say goodbye to stress<br>with in office massage</div>
  <div class="btn svc-btn abs" style="left:701px;top:754px">Book massage</div>
</section>

<section class="booking abs">
  <h2 class="section-title abs">Book a massage</h2>
  <form class="form-card abs">
    <div class="field select abs">Choose the type of massage
      <svg width="34" height="20" viewBox="0 0 34 20"><polyline points="2,3 17,17 32,3" fill="none" stroke="#1d1d1d" stroke-width="2.5"/></svg>
    </div>
    <div class="field input abs" style="top:140px">Name</div>
    <div class="field input abs" style="top:223px">Mobile</div>
    <div class="field input abs" style="top:304px">Email</div>
    <div class="field input abs" style="top:385px">Address</div>
    <div class="field input abs" style="top:466px">Date
      <div class="date-box abs" style="left:229px;top:9px">DD</div>
      <div class="date-box abs" style="left:293px;top:9px">MM</div>
    </div>
    <div class="btn book-btn abs">Book Now</div>
  </form>
</section>

<footer class="footer abs" role="img" aria-label="Soft-focus photo of massage oils and towels">
  <div class="contact abs">
    <div class="label">Contact me at</div>
    <div>lowenia@example.com</div>
    <div>0170-4410-93</div>
    <div class="social"><span></span><span></span><span></span><span></span></div>
  </div>
  <div class="address abs">
    <div class="label">Address</div>
    <div>xxxxxxxxxx</div>
    <div>xxxxxxxxxx</div>
    <div>xxx</div>
    <div>xxxxxxxxxx</div>
    <div>xxxxxxxxxx</div>
  </div>
</footer>
</body>
</html>
```